Profesional personal website needs design and business card

I need a business card with my professional name as a logo "Marlo Vitality" for my business. I am a Wellness Coach, consultant and trainer. So it should be professional, wellness oriented and modern.

Target Market(s)

Private clients, governments, corporations. Luxury and high market.

Industry/Entity Type

Health And Wellness

Contact Information for Business Card

Marlo Vitality should be the logo

Colors

Designer to choose colors to be used in the design.

Requirements
Must have
• Marlo Vitality
• Name: Tomás Arribal
• Wellness Coach, Consultant & Trainer.
• Website: www.marlovitality.example
• Phone:
• Spain (+34) 612 480 397
• (USA) +1 (555) 318 2046
Nice to have
• The most important is the design of "Marlo Vitality", as this is going to be my personal brand logo. It should be professional, wellness, high end and actual.
Should not have
• no golds, no baroque style..

```html
<!DOCTYPE html>
<html lang="en">
<head>
<meta charset="UTF-8">
<title>Marlo Vitality — Business Card</title>
<link rel="stylesheet" href="https://fonts.googleapis.com/css2?family=Roboto:wght@400;700;900&display=swap">
<style>
  :root {
    --stage: #2b2c2e;
    --card: #1b1c1e;
    --brand-green: #3cba35;
    --rule-green: #2c9a27;
    --ink-light: #e6e6e6;
  }
  * { margin: 0; padding: 0; box-sizing: border-box; }
  html, body {
    width: 1200px;
    height: 874px;
    overflow: hidden;
    background: var(--stage);
    font-family: "Roboto", Arial, sans-serif;
  }
  .stage {
    width: 1200px;
    height: 874px;
    display: flex;
    flex-direction: column;
    align-items: center;
    justify-content: center;
    gap: 40px;
  }
  .card {
    width: 620px;
    height: 354px;
    background: var(--card);
    display: flex;
    flex-direction: column;
    align-items: center;
    justify-content: center;
    text-align: center;
    box-shadow: 0 6px 18px rgba(0,0,0,0.35);
  }
  .brand-name {
    color: var(--brand-green);
    font-weight: 900;
    text-transform: uppercase;
    line-height: 0.95;
    letter-spacing: 1px;
  }
  .card--front .brand-name { font-size: 64px; }
  .card--back { justify-content: flex-start; padding-top: 62px; }
  .card--back .brand-name { font-size: 40px; margin-bottom: 22px; }
  .person-name {
    color: var(--brand-green);
    font-weight: 700;
    font-size: 22px;
    text-transform: uppercase;
    letter-spacing: 0.5px;
  }
  .person-role {
    color: var(--ink-light);
    font-size: 14px;
    text-transform: uppercase;
    margin-top: 4px;
    letter-spacing: 0.3px;
  }
  .contact-rule {
    width: 420px;
    height: 1px;
    background: var(--rule-green);
    margin: 10px 0;
  }
  .contact-phones {
    color: var(--ink-light);
    font-size: 16px;
    text-transform: uppercase;
  }
  .contact-phones .divider { margin: 0 8px; }
  .contact-web {
    color: var(--ink-light);
    font-size: 16px;
    text-transform: uppercase;
    margin-top: 4px;
  }
</style>
</head>
<body>
<main class="stage">
  <section class="card card--front" aria-label="Card front">
    <div class="brand-name">Marlo<br>Vitality</div>
  </section>

  <section class="card card--back" aria-label="Card back">
    <div class="brand-name">Marlo<br>Vitality</div>
    <div class="person-name">Tomás Arribal</div>
    <div class="person-role">Wellness Coach, Consultant &amp; Trainer</div>
    <div class="contact-rule"></div>
    <div class="contact-phones">(+34) 612 480 397 Spain<span class="divider">|</span>+1 (555) 318 2046 (USA)</div>
    <div class="contact-rule"></div>
    <div class="contact-web">www.marlovitality.example</div>
  </section>
</main>
</body>
</html>
```